Corporate Design für fenno-atelier
Zielgruppe
personalisierbare bedruckte Artikel
Geschenkverpackung
Designprodukte
papierdesign
Zielgruppe moderne Junge Menschen 20-40 Jahre, mit und ohne Kindern, aktiv in Leben, eher Stadtbewohner
Aufgabenstellung
Das design muss universell einsetzbar sein, soll cool, modern aber trotzdem etwas verspielt sein. Soll für Kinderkollektion und Erwachsenen Kollektion geeignet sein. Die Marke fenno-atelier muss nicht unbediengt ganz groß ausgeschrieben sein.Alle unsere Artikel sind z. B. bei kaufora zu finden, bitte bei der Suche fenno-atelier eintragen.

```html
<!DOCTYPE html>
<html lang="de">
<head>
<meta charset="utf-8">
<title>fenno-atelier – Geschäftsausstattung</title>
<link rel="stylesheet" href="https://fonts.googleapis.com/css2?family=Roboto+Condensed:wght@400;700&display=swap">
<style>
  :root {
    --teal: #57b0b3;
    --teal-light: #8ccbcd;
    --magenta: #bf5686;
    --magenta-light: #d684a9;
    --green: #97b674;
    --green-light: #b9cfa0;
    --ink: #444444;
    --paper: #ffffff;
    --paper-warm: #faf8f4;
    --rule: #c98a9e;
    --stage: #ffffff;
  }
  * { box-sizing: border-box; margin: 0; padding: 0; }
  html, body { width: 1200px; height: 1195px; overflow: hidden; background: var(--stage); }
  body { position: relative; font-family: "Roboto Condensed", sans-serif; color: var(--ink); }

  /* Business cards */
  .card {
    position: absolute;
    left: 60px;
    width: 380px;
    height: 245px;
    overflow: hidden;
    box-shadow: 0 1px 4px rgba(0,0,0,0.18);
  }
  .card--teal { top: 60px; background: var(--teal); }
  .card--magenta { top: 335px; background: var(--magenta); }
  .card--green { top: 610px; background: var(--green); }
  .card--contact { top: 885px; background: var(--paper); }

  .card__pattern {
    position: absolute; left: 0; top: 0; width: 100%; height: 70px;
  }
  .card--teal .card__pattern { background: linear-gradient(var(--teal-light), var(--teal)); }
  .card--magenta .card__pattern { background: linear-gradient(var(--magenta-light), var(--magenta)); }
  .card--green .card__pattern { background: linear-gradient(var(--green-light), var(--green)); }

  .brand {
    position: absolute;
    display: flex; align-items: center; gap: 8px;
    font-weight: 400;
    white-space: nowrap;
  }
  .brand__dot { width: 14px; height: 14px; border-radius: 50%; background: currentColor; }
  .card .brand { left: 50%; top: 125px; transform: translateX(-50%); font-size: 34px; color: #fff; }

  .card__band { position: absolute; left: 0; top: 0; width: 100%; height: 16px; background: var(--teal); }
  .card--contact .brand { top: 48px; color: var(--ink); font-size: 30px; }
  .card__address, .card__phone {
    position: absolute; top: 140px; font-size: 15px; line-height: 1.4;
  }
  .card__address { left: 34px; }
  .card__phone { left: 200px; top: 160px; }

  /* Letterhead */
  .letterhead {
    position: absolute;
    left: 490px; top: 124px;
    width: 660px; height: 933px;
    background: linear-gradient(var(--paper) 55%, var(--paper-warm));
    box-shadow: 0 1px 6px rgba(0,0,0,0.18);
  }
  .letterhead__stripe { position: absolute; top: 0; left: 0; height: 19px; display: flex; width: 100%; }
  .letterhead__stripe span:nth-child(1) { width: 374px; background: var(--teal); }
  .letterhead__stripe span:nth-child(2) { width: 141px; background: var(--magenta); }
  .letterhead__stripe span:nth-child(3) { flex: 1; background: var(--green); }

  .letterhead .brand { right: 50px; top: 150px; font-size: 32px; color: var(--ink); }

  .sender-line {
    position: absolute; left: 72px; top: 166px; width: 240px;
    display: flex; justify-content: space-between;
    font-size: 9.5px; padding-bottom: 2px;
    border-bottom: 0.7px solid #999;
  }
  .sender-line strong { font-weight: 700; }

  .footer-info {
    position: absolute; left: 503px; top: 728px; height: 190px;
    border-left: 0.7px solid var(--rule);
    padding-left: 17px;
    font-size: 9.5px; line-height: 1.42;
  }
  .footer-info p + p { margin-top: 7px; }
</style>
</head>
<body>

  <section class="card card--teal" aria-label="Visitenkarte Vorderseite Türkis">
    <div class="card__pattern" role="img" aria-label="Punktmuster in hellem Türkis"></div>
    <div class="brand"><span class="brand__dot"></span>fenno-atelier</div>
  </section>

  <section class="card card--magenta" aria-label="Visitenkarte Vorderseite Magenta">
    <div class="card__pattern" role="img" aria-label="Punktmuster in hellem Magenta"></div>
    <div class="brand"><span class="brand__dot"></span>fenno-atelier</div>
  </section>

  <section class="card card--green" aria-label="Visitenkarte Vorderseite Grün">
    <div class="card__pattern" role="img" aria-label="Punktmuster in hellem Grün"></div>
    <div class="brand"><span class="brand__dot"></span>fenno-atelier</div>
  </section>

  <section class="card card--contact" aria-label="Visitenkarte Rückseite">
    <div class="card__band"></div>
    <div class="brand"><span class="brand__dot"></span>fenno-atelier</div>
    <p class="card__address">Max Mustermann<br>Musterstraße 12<br>12345 Musterstadt</p>
    <p class="card__phone">T. 0123 456 789<br>F. 0123 456 789<br>info@fenno-atelier.example</p>
  </section>

  <section class="letterhead" aria-label="Briefbogen">
    <div class="letterhead__stripe"><span></span><span></span><span></span></div>
    <div class="sender-line">
      <strong>Max Mustermann</strong><span>Musterstraße 00</span><span>0000 Musterstadt</span>
    </div>
    <div class="brand"><span class="brand__dot"></span>fenno-atelier</div>
    <div class="footer-info">
      <p>Max Mustermann<br>Musterstraße 12<br>12345 Musterstadt</p>
      <p>T. 0123 456 789<br>F. 0123 456 789<br>info@fenno-atelier.example</p>
      <p>Bank&nbsp;&nbsp;&nbsp;Musterbank<br>BLZ&nbsp;&nbsp;&nbsp;&nbsp;&nbsp;xxx xxx xxx<br>Kto-Nr. Xxx xxx xxx</p>
      <p>Registergericht Amtsgericht<br>St.-Nr. Xxxxx xxxx xxxx<br>USt.-Id-Nr. DE xxxxxxxxx</p>
    </div>
  </section>

</body>
</html>
```